The Willow Hearth: Steady Horizon

Please use the attached images as a reference and as inspiration for this contest. Please note, these images are google searched and belong to someone else.
This project is for our church.
We have a new Sermon Series launching and we want to be able to promote it and manipulate the size of the project via Facebook Cover Art, CD Labels, T-Shirts, Banners, etc.
Requesting a HD 1080 X 920 pixels.
Need an editable PSD file from the winner of the contest.
The title of the project is: Steady Horizon.
The idea behind this project is bringing things in life into focus to help our congregation be intentional about focusing on making positive changes to major areas of life.
When we think of this - we think of a camera brining something into focus to take that perfect shot, or as one of the attached images show blurry images coming into focus.
Keywords that can be used in the design are: Faith, Family, Finances, and Fitness.
Just because it is for a church does NOT mean we need it to look like its for a church. In fact, we desire the design to be compelling to someone who has never stepped foot into a church building. Avoid a "church" look.
Good Luck!
Target Market(s)
Everyone
Industry/Entity Type
House
Requirements
Must have
- Bringing "things" into focus.
- Please read description for more details
Should not have
- A church look

```html
<!DOCTYPE html>
<html lang="en">
<head>
<meta charset="utf-8">
<title>Steady Horizon – The Willow Hearth</title>
<link href="https://fonts.googleapis.com/css2?family=Nanum+Pen+Script&family=Permanent+Marker&display=swap" rel="stylesheet">
<style>
  :root {
    --navy-deep: #040b16;
    --navy: #0c1b2c;
    --teal-dark: #12303a;
    --olive: #5f6a2e;
    --green: #3f7a36;
    --rust: #5a3a2c;
    --title-light: #e4e4e4;
    --title-shade: #8d8d8d;
    --title-green: #0f3a30;
    --title-red: #b43a2a;
    --subtitle: #f2f2f2;
  }
  * { margin: 0; padding: 0; box-sizing: border-box; }
  html, body { width: 1200px; height: 1022px; overflow: hidden; background: var(--navy-deep); }
  .cover {
    position: relative;
    width: 1200px;
    height: 1022px;
    overflow: hidden;
    background: var(--navy-deep);
  }
  .prism-field {
    position: absolute;
    inset: 0;
    background:
      radial-gradient(ellipse 260px 380px at 600px 860px, rgba(90,140,60,0.75), transparent 70%),
      radial-gradient(ellipse 200px 220px at 600px 340px, rgba(110,120,50,0.55), transparent 75%),
      radial-gradient(ellipse 330px 420px at 600px 420px, rgba(90,55,40,0.45), transparent 75%),
      radial-gradient(ellipse 560px 640px at 600px 560px, rgba(25,60,60,0.85), transparent 80%),
      linear-gradient(90deg, var(--navy-deep) 0%, var(--navy) 30%, var(--teal-dark) 50%, var(--navy) 70%, var(--navy-deep) 100%);
  }
  .series-title {
    position: absolute;
    left: 0;
    width: 1200px;
    text-align: center;
  }
  .series-title__top {
    top: 372px;
    font-family: "Nanum Pen Script", cursive;
    font-size: 160px;
    line-height: 1;
    color: var(--title-light);
    text-shadow: 3px 3px 0 var(--title-shade);
    letter-spacing: 2px;
  }
  .series-title__bottom {
    top: 518px;
    font-family: "Permanent Marker", cursive;
    font-size: 118px;
    line-height: 1;
    color: var(--title-green);
    text-shadow: -4px -3px 0 var(--title-red);
    letter-spacing: 6px;
  }
  .series-tagline {
    position: absolute;
    top: 662px;
    left: 0;
    width: 1200px;
    text-align: center;
    font-family: Arial, Helvetica, sans-serif;
    font-style: italic;
    font-size: 18px;
    color: var(--subtitle);
    letter-spacing: 0.3px;
  }
</style>
</head>
<body>
  <main class="cover">
    <div class="prism-field" role="img" aria-label="Abstract pattern of overlapping translucent triangles and circles in navy, olive, rust and green converging on the centre"></div>
    <h1>
      <span class="series-title series-title__top">Steady</span>
      <span class="series-title series-title__bottom">HORIZON</span>
    </h1>
    <p class="series-tagline">A 3 WEEK SERIES ON FAITH, FAMILY, FINANCES AND FITNESS</p>
  </main>
</body>
</html>
```